Sherwood Ads

Would like to have new web ads announcing opening of a new pediatric office (Brightfern Pediatrics - Sherwood). First and only dedicated pediatric clinic in Sherwood. Ads need to be following sizes: 160x160, 180x180, 300x250, 336x280, 728x90, 920x250, 1080x1080, 1200x627. Sample of previous ad attached.

```html
<!DOCTYPE html>
<html lang="en">
<head>
<meta charset="utf-8">
<title>Sherwood Ads – Brightfern Pediatrics</title>
<link rel="stylesheet" href="https://fonts.googleapis.com/css2?family=Roboto+Condensed:wght@400;700&family=Nunito:wght@700;800&display=swap">
<style>
:root{
  --stage:#4e2e1c;
  --paper:#f6f6f6;
  --red:#ee3a2c;
  --blue:#2b51b3;
  --navy:#2c4aa6;
  --brand:#5753c6;
  --yellow:#f6c81a;
  --ink:#222;
  --label:#f3ece6;
}
*{margin:0;padding:0;box-sizing:border-box}
html,body{width:1200px;height:535px;overflow:hidden;background:var(--stage)}
.board{position:relative;width:1200px;height:535px;font-family:"Roboto Condensed",Arial,sans-serif}
.ad{position:absolute;background:var(--paper);overflow:hidden}
.ad > *{position:absolute}
.size-label{position:absolute;color:var(--label);font-family:"Roboto Condensed",Arial,sans-serif;font-size:10.5px;letter-spacing:.3px}
.new{color:var(--red);font-weight:700;display:flex;align-items:center;line-height:1;white-space:nowrap}
.new svg{margin-right:.12em}
.title{color:var(--navy);font-weight:700;line-height:1.05;white-space:nowrap}
.title .place{color:var(--red)}
.brand{color:var(--brand);font-family:"Nunito",Arial,sans-serif;font-weight:800;line-height:.95;display:flex;align-items:center;white-space:nowrap}
.brand .dot{border-radius:50%;background:var(--brand);flex:none}
.svc{display:flex;align-items:flex-start;color:var(--ink);line-height:1.1;white-space:nowrap}
.ico{border-radius:50%;flex:none;display:flex;align-items:center;justify-content:center}
.ico svg{width:62%;height:62%}
.ico-heart{background:var(--red)}
.ico-tele{background:#4a74d0}
.ico-care{background:var(--yellow)}
.wave{left:0;top:0}
.book{background:#fff;border-radius:4px;color:var(--blue);font-family:"Nunito",Arial,sans-serif;font-weight:700;display:flex;align-items:center;justify-content:center;white-space:nowrap}
.book-mini{color:#fff;font-family:"Nunito",Arial,sans-serif;font-weight:700;display:flex;align-items:center;white-space:nowrap}
.pill-red{background:var(--red);color:#fff;font-weight:700;white-space:nowrap;display:flex;align-items:center;padding-left:.5em}
.pill-blue{background:var(--blue);color:#fff;white-space:nowrap;display:flex;align-items:center;justify-content:center;clip-path:polygon(4% 0,100% 0,96% 100%,0 100%)}
.opening{color:var(--navy);font-weight:700;text-decoration:underline;white-space:nowrap}
.opening .place{color:var(--red)}
.photo{border-radius:50%;border:solid var(--yellow);background:radial-gradient(circle at 45% 45%,#e9b98f 0%,#c98d62 28%,#f0c640 55%,#8cb6e0 80%,#cfe1f3 100%)}
.photo-strip{background:linear-gradient(90deg,#cfe1f3,#e0b086 40%,#b97f58 65%,#f0c640)}
.big-brand{left:38px;top:412px;gap:14px;font-size:36px}
.big-brand .dot{width:62px;height:62px}
</style>
</head>
<body>
<main class="board">

  <!-- 160x160 -->
  <section class="ad" style="left:26px;top:39px;width:52px;height:51px">
    <div class="new" style="left:3px;top:3px;font-size:6px"><svg width="4" height="5" viewBox="0 0 10 10"><path d="M2 1 7 5M1 5 6 8" stroke="#ee3a2c" stroke-width="2"/></svg>NEW</div>
    <div class="title" style="left:3px;top:11px;font-size:4.2px;font-weight:400">CLINIC COMING<br>TO SHERWOOD, OR</div>
    <div class="pill-red" style="left:2px;top:24px;width:43px;height:5px;font-size:3.3px">Opening In July 2026</div>
    <div class="brand" style="left:3px;top:34px;font-size:3.6px;gap:2px"><span class="dot" style="width:6px;height:6px"></span><span>Brightfern<br>Pediatrics</span></div>
    <svg class="wave" width="52" height="51" viewBox="0 0 52 51" preserveAspectRatio="none"><path d="M0 50 C20 48 30 40 52 39 V51 H0Z" fill="#ee3a2c"/><path d="M10 51 C24 48 34 42 52 41 V51Z" fill="#2b51b3"/></svg>
  </section>
  <div class="size-label" style="left:27px;top:96px">160x160</div>

  <!-- 180x180 -->
  <section class="ad" style="left:94px;top:39px;width:58px;height:58px">
    <div class="new" style="left:3px;top:3px;font-size:6.5px"><svg width="4" height="5" viewBox="0 0 10 10"><path d="M2 1 7 5M1 5 6 8" stroke="#ee3a2c" stroke-width="2"/></svg>NEW</div>
    <div class="title" style="left:3px;top:12px;font-size:4.6px;font-weight:400">CLINIC COMING<br>TO SHERWOOD, OR</div>
    <div class="pill-red" style="left:2px;top:26px;width:48px;height:6px;font-size:3.6px">Opening In July 2026</div>
    <div class="brand" style="left:3px;top:38px;font-size:4px;gap:2px"><span class="dot" style="width:7px;height:7px"></span><span>Brightfern<br>Pediatrics</span></div>
    <svg class="wave" width="58" height="58" viewBox="0 0 58 58" preserveAspectRatio="none"><path d="M0 57 C22 55 34 45 58 44 V58 H0Z" fill="#ee3a2c"/><path d="M10 58 C26 55 38 47 58 46 V58Z" fill="#2b51b3"/></svg>
  </section>
  <div class="size-label" style="left:97px;top:99px">180x180</div>

  <!-- 300x250 -->
  <section class="ad" style="left:172px;top:39px;width:97px;height:81px">
    <div class="new" style="left:6px;top:5px;font-size:9px"><svg width="5" height="7" viewBox="0 0 10 10"><path d="M2 1 7 5M1 5 6 8" stroke="#ee3a2c" stroke-width="2"/></svg>NEW</div>
    <div class="title" style="left:6px;top:15px;font-size:7px;font-weight:400">CLINIC COMING<br>TO SHERWOOD, OR</div>
    <div class="pill-red" style="left:5px;top:33px;width:62px;height:8px;font-size:5.5px">Opening In July 2026</div>
    <div class="brand" style="left:5px;top:50px;font-size:6px;gap:3px"><span class="dot" style="width:10px;height:10px"></span><span>Brightfern<br>Pediatrics</span></div>
    <svg class="wave" width="97" height="81" viewBox="0 0 97 81" preserveAspectRatio="none"><path d="M0 78 C38 76 58 62 97 60 V81 H0Z" fill="#ee3a2c"/><path d="M0 81 C40 79 60 65 97 63 V81Z" fill="#2b51b3"/></svg>
    <div class="book-mini" style="left:58px;top:72px;font-size:4.5px;gap:1px"><svg width="5" height="5" viewBox="0 0 10 10"><rect x="1" y="2" width="8" height="7" fill="none" stroke="#fff"/></svg>Book A Visit</div>
  </section>
  <div class="size-label" style="left:169px;top:124px">300x250</div>

  <!-- 336x280 -->
  <section class="ad" style="left:283px;top:39px;width:109px;height:90px">
    <div class="new" style="left:6px;top:4px;font-size:10px"><svg width="6" height="7" viewBox="0 0 10 10"><path d="M2 1 7 5M1 5 6 8" stroke="#ee3a2c" stroke-width="2"/></svg>NEW</div>
    <div class="title" style="left:6px;top:17px;font-size:7.5px">Clinic Coming- To <span class="place">Sherwood, OR</span></div>
    <div class="svc" style="left:8px;top:30px;font-size:7px;gap:4px;align-items:center"><span class="ico ico-heart" style="width:10px;height:10px"><svg viewBox="0 0 20 20"><path d="M10 16 4 10A3.3 3.3 0 0 1 10 5.5 3.3 3.3 0 0 1 16 10Z" fill="none" stroke="#fff" stroke-width="2"/></svg></span>Behavioral Health</div>
    <div class="svc" style="left:8px;top:43px;font-size:7px;gap:4px;align-items:center"><span class="ico ico-tele" style="width:10px;height:10px"><svg viewBox="0 0 20 20"><rect x="4" y="5" width="12" height="8" fill="none" stroke="#fff" stroke-width="2"/><path d="M7 16h6" stroke="#fff" stroke-width="2"/></svg></span>Telehealth</div>
    <div class="svc" style="left:8px;top:56px;font-size:7px;gap:4px;align-items:center"><span class="ico ico-care" style="width:10px;height:10px"><svg viewBox="0 0 20 20"><path d="M10 4v12M4 10h12" stroke="#fff" stroke-width="3"/></svg></span>Pediatric Primary Care</div>
    <svg class="wave" width="109" height="90" viewBox="0 0 109 90" preserveAspectRatio="none"><path d="M0 85 C42 83 66 70 109 68 V90 H0Z" fill="#ee3a2c"/><path d="M0 88 C44 86 68 73 109 71 V90Z" fill="#2b51b3"/></svg>
    <div class="book-mini" style="left:65px;top:80px;font-size:5.5px;gap:1px"><svg width="6" height="6" viewBox="0 0 10 10"><rect x="1" y="2" width="8" height="7" fill="none" stroke="#fff"/></svg>Book A Visit</div>
  </section>
  <div class="size-label" style="left:283px;top:137px">336x280</div>

  <!-- 728x90 -->
  <section class="ad" style="left:28px;top:186px;width:236px;height:29px">
    <div class="new" style="left:3px;top:2px;font-size:5.5px"><svg width="3" height="4" viewBox="0 0 10 10"><path d="M2 1 7 5M1 5 6 8" stroke="#ee3a2c" stroke-width="2"/></svg>NEW</div>
    <div class="title" style="left:4px;top:9px;font-size:7.5px">Clinic Coming- To <span class="place">Sherwood, OR</span></div>
    <div class="opening" style="left:4px;top:20px;font-size:5px">OPENING IN <span class="place">JULY</span> 2026</div>
    <div class="brand" style="left:108px;top:7px;font-size:7.5px;gap:3px"><span class="dot" style="width:12px;height:12px"></span><span>Brightfern<br>Pediatrics</span></div>
    <div class="photo-strip" role="img" aria-label="Photo of smiling children in a huddle looking down at the camera" style="left:186px;top:0;width:50px;height:29px;border-radius:40px 0 0 40px / 29px 0 0 29px"></div>
    <svg class="wave" width="236" height="29" viewBox="0 0 236 29" preserveAspectRatio="none"><path d="M178 29 C200 27 215 24 236 22 V29Z" fill="#2b51b3"/></svg>
  </section>
  <div class="size-label" style="left:32px;top:220px">728x90</div>

  <!-- 920x250 -->
  <section class="ad" style="left:26px;top:271px;width:299px;height:81px">
    <div class="new" style="left:8px;top:3px;font-size:6px"><svg width="4" height="5" viewBox="0 0 10 10"><path d="M2 1 7 5M1 5 6 8" stroke="#ee3a2c" stroke-width="2"/></svg>NEW</div>
    <div class="title" style="left:8px;top:14px;font-size:9px">CLINIC COMING- TO <span class="place">SHERWOOD, OR</span></div>
    <div class="opening" style="left:8px;top:30px;font-size:5.8px;display:flex;align-items:center;gap:3px"><svg width="7" height="7" viewBox="0 0 10 10"><path d="M5 0 6.2 3.6 10 3.8 7 6.1 8 10 5 7.7 2 10 3 6.1 0 3.8 3.8 3.6Z" fill="#2c4aa6"/></svg><span>OPENING IN <span class="place">JULY</span> 2026</span></div>
    <div class="svc" style="left:9px;top:42px;font-size:7px;gap:4px;align-items:center"><span class="ico ico-heart" style="width:10px;height:10px"><svg viewBox="0 0 20 20"><path d="M10 16 4 10A3.3 3.3 0 0 1 10 5.5 3.3 3.3 0 0 1 16 10Z" fill="none" stroke="#fff" stroke-width="2"/></svg></span>Behavioral Health</div>
    <div class="svc" style="left:82px;top:38px;font-size:7px;gap:4px;align-items:center"><span class="ico ico-care" style="width:10px;height:10px"><svg viewBox="0 0 20 20"><path d="M10 4v12M4 10h12" stroke="#fff" stroke-width="3"/></svg></span>Pediatric Primary Care</div>
    <div class="brand" style="left:9px;top:58px;font-size:7px;gap:3px"><span class="dot" style="width:12px;height:12px"></span><span>Brightfern<br>Pediatrics</span></div>
    <div class="photo" role="img" aria-label="Photo of smiling children in a huddle looking down at the camera" style="left:162px;top:-45px;width:170px;height:120px;border-width:2px"></div>
    <svg class="wave" width="299" height="81" viewBox="0 0 299 81" preserveAspectRatio="none"><path d="M140 81 C190 66 240 54 299 50 V81Z" fill="#ee3a2c"/><path d="M150 81 C198 69 244 57 299 53 V81Z" fill="#5753c6"/></svg>
  </section>
  <div class="size-label" style="left:28px;top:357px">920x250</div>

  <!-- brand name, large -->
  <div class="brand big-brand" style="position:absolute"><span class="dot"></span><span>Brightfern<br>Pediatrics</span></div>

  <!-- 1200x627 top -->
  <section class="ad" style="left:402px;top:39px;width:389px;height:203px">
    <div class="new" style="left:12px;top:7px;font-size:29px"><svg width="14" height="20" viewBox="0 0 10 14"><path d="M3 1 8 6M1 7 7 10M3 12.5 7 13" stroke="#ee3a2c" stroke-width="1.8"/></svg>NEW</div>
    <div class="title" style="left:12px;top:42px;font-size:20.5px">CLINIC COMING- TO <span class="place">SHERWOOD, OR</span></div>
    <div class="svc" style="left:10px;top:73px;font-size:17px;gap:8px"><span class="ico ico-heart" style="width:24px;height:24px"><svg viewBox="0 0 20 20"><path d="M10 16 4 10A3.3 3.3 0 0 1 10 5.5 3.3 3.3 0 0 1 16 10Z" fill="none" stroke="#fff" stroke-width="2"/></svg></span><span>Behavioral<br>Health</span></div>
    <div class="svc" style="left:125px;top:73px;font-size:17px;gap:8px"><span class="ico ico-tele" style="width:24px;height:24px"><svg viewBox="0 0 20 20"><rect x="4" y="5" width="12" height="8" fill="none" stroke="#fff" stroke-width="1.6"/><path d="M7 16h6" stroke="#fff" stroke-width="1.6"/></svg></span><span>Telehealth</span></div>
    <div class="svc" style="left:246px;top:73px;font-size:17px;gap:9px"><span class="ico ico-care" style="width:24px;height:24px"><svg viewBox="0 0 20 20"><path d="M10 4v12M4 10h12" stroke="#fff" stroke-width="3"/></svg></span><span>Pediatric<br>Primary Care</span></div>
    <div class="brand" style="left:10px;top:122px;font-size:15px;gap:7px"><span class="dot" style="width:28px;height:28px"></span><span>Brightfern<br>Pediatrics</span></div>
    <svg class="wave" width="389" height="203" viewBox="0 0 389 203" preserveAspectRatio="none"><path d="M0 182 C150 178 230 136 389 136 V203 H0Z" fill="#ee3a2c"/><path d="M0 187 C152 183 232 142 389 142 V203 H0Z" fill="#2b51b3"/></svg>
    <div class="book" style="left:240px;top:156px;width:134px;height:41px;font-size:16px;gap:5px"><svg width="22" height="22" viewBox="0 0 24 24"><rect x="2" y="4" width="17" height="16" rx="2" fill="none" stroke="#2b51b3" stroke-width="1.8"/><path d="M6 2v4M15 2v4M2 9h17" stroke="#2b51b3" stroke-width="1.8"/><circle cx="18" cy="18" r="4.5" fill="#fff" stroke="#2b51b3" stroke-width="1.6"/><path d="M18 16v2.2l1.4 1" stroke="#2b51b3" stroke-width="1.4" fill="none"/></svg>Book A Visit</div>
  </section>
  <div class="size-label" style="left:403px;top:252px">1200x627</div>

  <!-- 1200x627 bottom -->
  <section class="ad" style="left:402px;top:279px;width:389px;height:204px">
    <div class="new" style="left:13px;top:12px;font-size:27px"><svg width="13" height="18" viewBox="0 0 10 14"><path d="M3 1 8 6M1 7 7 10M3 12.5 7 13" stroke="#ee3a2c" stroke-width="1.8"/></svg>NEW</div>
    <div class="pill-blue" style="left:98px;top:14px;width:162px;height:24px;font-size:15px">Opening In July 2026</div>
    <svg style="left:263px;top:15px" width="14" height="22" viewBox="0 0 14 22"><path d="M2 8 12 3M2 11h11M2 14 12 19" stroke="#2b51b3" stroke-width="2"/></svg>
    <div class="title" style="left:13px;top:46px;font-size:18.5px">CLINIC COMING- TO <span class="place">SHERWOOD, OR</span></div>
    <div class="svc" style="left:11px;top:77px;font-size:14px;gap:6px"><span class="ico ico-heart" style="width:19px;height:19px"><svg viewBox="0 0 20 20"><path d="M10 16 4 10A3.3 3.3 0 0 1 10 5.5 3.3 3.3 0 0 1 16 10Z" fill="none" stroke="#fff" stroke-width="2"/></svg></span><span>Behavioral<br>Health</span></div>
    <div class="svc" style="left:98px;top:77px;font-size:14px;gap:6px"><span class="ico ico-tele" style="width:19px;height:19px"><svg viewBox="0 0 20 20"><rect x="4" y="5" width="12" height="8" fill="none" stroke="#fff" stroke-width="1.6"/><path d="M7 16h6" stroke="#fff" stroke-width="1.6"/></svg></span><span>Telehealth</span></div>
    <div class="svc" style="left:190px;top:77px;font-size:14px;gap:6px"><span class="ico ico-care" style="width:19px;height:19px"><svg viewBox="0 0 20 20"><path d="M10 4v12M4 10h12" stroke="#fff" stroke-width="3"/></svg></span><span>Pediatric<br>Primary Care</span></div>
    <div class="photo" role="img" aria-label="Photo of smiling children in a huddle looking down at the camera" style="left:280px;top:-40px;width:230px;height:210px;border-width:4px"></div>
    <div class="brand" style="left:11px;top:126px;font-size:15px;gap:7px"><span class="dot" style="width:28px;height:28px"></span><span>Brightfern<br>Pediatrics</span></div>
    <svg class="wave" width="389" height="204" viewBox="0 0 389 204" preserveAspectRatio="none"><path d="M0 182 C150 178 230 136 389 134 V204 H0Z" fill="#ee3a2c"/><path d="M0 187 C152 183 232 142 389 140 V204 H0Z" fill="#2b51b3"/></svg>
    <div class="book" style="left:210px;top:155px;width:134px;height:41px;font-size:16px;gap:5px"><svg width="22" height="22" viewBox="0 0 24 24"><rect x="2" y="4" width="17" height="16" rx="2" fill="none" stroke="#2b51b3" stroke-width="1.8"/><path d="M6 2v4M15 2v4M2 9h17" stroke="#2b51b3" stroke-width="1.8"/><circle cx="18" cy="18" r="4.5" fill="#fff" stroke="#2b51b3" stroke-width="1.6"/><path d="M18 16v2.2l1.4 1" stroke="#2b51b3" stroke-width="1.4" fill="none"/></svg>Book A Visit</div>
  </section>
  <div class="size-label" style="left:402px;top:490px">1200x627</div>

  <!-- 1080x1080 -->
  <section class="ad" style="left:824px;top:37px;width:350px;height:350px">
    <div class="photo" role="img" aria-label="Photo of smiling children in a huddle looking down at the camera" style="left:162px;top:-20px;width:300px;height:300px;border-width:5px"></div>
    <div class="new" style="left:9px;top:27px;font-size:29px"><svg width="14" height="20" viewBox="0 0 10 14"><path d="M3 1 8 6M1 7 7 10M3 12.5 7 13" stroke="#ee3a2c" stroke-width="1.8"/></svg>NEW</div>
    <div class="title" style="left:10px;top:64px;font-size:24.5px">Clinic Coming To<br><span class="place">Sherwood, OR</span></div>
    <div class="svc" style="left:12px;top:130px;font-size:14.5px;gap:8px;align-items:center"><span class="ico ico-heart" style="width:19px;height:19px"><svg viewBox="0 0 20 20"><path d="M10 16 4 10A3.3 3.3 0 0 1 10 5.5 3.3 3.3 0 0 1 16 10Z" fill="none" stroke="#fff" stroke-width="2"/></svg></span>Behavioral Health</div>
    <div class="svc" style="left:12px;top:157px;font-size:14.5px;gap:8px;align-items:center"><span class="ico ico-tele" style="width:19px;height:19px"><svg viewBox="0 0 20 20"><rect x="4" y="5" width="12" height="8" fill="none" stroke="#fff" stroke-width="1.6"/><path d="M7 16h6" stroke="#fff" stroke-width="1.6"/></svg></span>Telehealth</div>
    <div class="svc" style="left:12px;top:184px;font-size:14.5px;gap:8px;align-items:center"><span class="ico ico-care" style="width:19px;height:19px"><svg viewBox="0 0 20 20"><path d="M10 4v12M4 10h12" stroke="#fff" stroke-width="3"/></svg></span>Pediatric Primary Care</div>
    <div class="brand" style="left:9px;top:228px;font-size:20px;gap:10px"><span class="dot" style="width:38px;height:38px"></span><span>Brightfern<br>Pediatrics</span></div>
    <svg class="wave" width="350" height="350" viewBox="0 0 350 350" preserveAspectRatio="none"><path d="M0 322 C130 318 210 272 350 270 V350 H0Z" fill="#ee3a2c"/><path d="M0 327 C132 323 212 278 350 276 V350 H0Z" fill="#2b51b3"/></svg>
    <div class="book" style="left:204px;top:295px;width:134px;height:41px;font-size:16px;gap:5px"><svg width="22" height="22" viewBox="0 0 24 24"><rect x="2" y="4" width="17" height="16" rx="2" fill="none" stroke="#2b51b3" stroke-width="1.8"/><path d="M6 2v4M15 2v4M2 9h17" stroke="#2b51b3" stroke-width="1.8"/><circle cx="18" cy="18" r="4.5" fill="#fff" stroke="#2b51b3" stroke-width="1.6"/><path d="M18 16v2.2l1.4 1" stroke="#2b51b3" stroke-width="1.4" fill="none"/></svg>Book A Visit</div>
  </section>
  <div class="size-label" style="left:824px;top:396px">1080x1080</div>

</main>
</body>
</html>
```